Become a real French Pastry chef with an easy 3 step pastry kit box.

The company is specialized in French pastries and the boxes will be sold online, and retail stores. The goal is for anyone who likes to be creative and crafty to create and bake their own traditional french pastry in 3 easy steps right at home. French pastries can be known to take hours to bake. These boxes allow you to make them very quickly, no hassle and they results taste amazing. All the ingredients are from FRANCE. Everything you need is in the box, All you need is water! The box design desired is elegant, simple, glamorous but yet eye catchy for retail distribution. This is a kit box with pre scaled ingredients to make your own eclairs. Box dimensions are 8x6x2.
Updates

Target Market(s)

Middle Aged, middle to upper class housewives who enjoy cooking and baking

Industry/Entity Type

Bakery

Font styles to use
Decorative
Script

Colors

Designer to choose colors to be used in the design.

Requirements
Must have
• This box will be called "The eclair kit by {logo}, or {logo} presents the Eclair kit.
• Has to have the instructions (attached document)
• "This box contains: 4 éclair shells, powder pouch, icing bag, pipping bag and pipping tip"
• Net weight 245g
• Nutrition label (attached)
Nice to have
• An eclair on it.

```html
<!DOCTYPE html>
<html lang="en">
<head>
<meta charset="utf-8">
<title>The Eclair Kit – Box Lid</title>
<link rel="stylesheet" href="https://fonts.googleapis.com/css2?family=Playfair+Display:wght@400;700&family=Yesteryear&display=swap">
<style>
  :root {
    --backdrop: #cfe4fb;
    --lid: #ffffff;
    --coral: #f0553a;
    --coral-title: #f08a78;
    --coral-wash: rgba(244, 140, 118, .22);
    --teal: #8fe3df;
    --teal-soft: #c9f3f0;
    --pastry: #e6cfae;
    --navy: #1d3a9e;
    --frame-blue: #7fb0e8;
    --ribbon: #f2f1ec;
    --ribbon-edge: #c9c7bf;
  }
  * { box-sizing: border-box; margin: 0; padding: 0; }
  html, body { width: 1200px; height: 1200px; overflow: hidden; }
  body { background: var(--backdrop); position: relative; }

  .lid {
    position: absolute; left: 100px; top: 225px;
    width: 1000px; height: 750px;
    background: var(--lid);
    box-shadow: 0 10px 30px rgba(40, 70, 110, .18);
  }

  .corner {
    position: absolute; width: 200px; height: 140px;
  }
  .corner.tl { left: 30px; top: 30px; }
  .corner.tr { right: 30px; top: 30px; transform: scaleX(-1); }
  .corner.bl { left: 30px; bottom: 30px; transform: scaleY(-1); }
  .corner.br { right: 30px; bottom: 30px; transform: scale(-1, -1); }
  .corner-ornament {
    position: absolute; left: 10px; top: 10px; width: 130px; height: 95px;
    background: radial-gradient(ellipse at 20% 20%, var(--coral-wash) 0%, rgba(255,255,255,0) 70%);
  }
  .corner-frame { position: absolute; left: 0; top: 0; }

  .watercolor-wash {
    position: absolute; left: 250px; top: 90px; width: 500px; height: 500px;
    background: radial-gradient(ellipse at 50% 50%, var(--teal) 0%, var(--teal-soft) 55%, rgba(255,255,255,0) 75%);
  }
  .kit-title {
    position: absolute; left: 0; right: 0; top: 158px; text-align: center;
    font-family: 'Playfair Display', serif; font-weight: 400; font-size: 32px; letter-spacing: 3px;
    color: var(--coral-title);
  }
  .dotted-band {
    position: absolute; left: 40px; right: 40px; top: 270px; height: 80px;
    background: var(--coral);
  }
  .brand-label {
    position: absolute; left: 340px; top: 235px; width: 320px; height: 150px;
    background: #fff; border: 4px solid var(--frame-blue); border-radius: 28px;
    display: flex; align-items: center; justify-content: center; gap: 12px;
  }
  .brand-dot { width: 16px; height: 16px; border-radius: 50%; background: var(--coral); }
  .brand-name {
    font-family: 'Playfair Display', serif; font-size: 30px; font-weight: 700;
    color: var(--navy); text-align: center; line-height: 1.1;
  }
  .eclair-art {
    position: absolute; top: 400px; width: 230px; height: 130px;
    background: linear-gradient(180deg, #d9a893 0%, var(--pastry) 60%, #f2e6d2 100%);
    border-radius: 40px;
  }
  .eclair-art.left { left: 270px; }
  .eclair-art.right { left: 520px; }
  .steps-banner { position: absolute; left: 330px; top: 565px; width: 340px; height: 80px; }
  .steps-text {
    position: absolute; left: 0; right: 0; top: 16px; text-align: center;
    font-family: 'Yesteryear', cursive; font-size: 36px; color: var(--coral);
  }
</style>
</head>
<body>
  <main class="lid">
    <div class="corner tl">
      <div class="corner-ornament" role="img" aria-label="Delicate coral scroll flourish"></div>
      <svg class="corner-frame" width="200" height="140" viewBox="0 0 200 140" aria-hidden="true">
        <path d="M2 138 V2 H198" fill="none" stroke="var(--coral)" stroke-width="2.5"/>
      </svg>
    </div>
    <div class="corner tr">
      <div class="corner-ornament" role="img" aria-label="Delicate coral scroll flourish"></div>
      <svg class="corner-frame" width="200" height="140" viewBox="0 0 200 140" aria-hidden="true">
        <path d="M2 138 V2 H198" fill="none" stroke="var(--coral)" stroke-width="2.5"/>
      </svg>
    </div>
    <div class="corner bl">
      <div class="corner-ornament" role="img" aria-label="Delicate coral scroll flourish"></div>
      <svg class="corner-frame" width="200" height="140" viewBox="0 0 200 140" aria-hidden="true">
        <path d="M2 138 V2 H198" fill="none" stroke="var(--coral)" stroke-width="2.5"/>
      </svg>
    </div>
    <div class="corner br">
      <div class="corner-ornament" role="img" aria-label="Delicate coral scroll flourish"></div>
      <svg class="corner-frame" width="200" height="140" viewBox="0 0 200 140" aria-hidden="true">
        <path d="M2 138 V2 H198" fill="none" stroke="var(--coral)" stroke-width="2.5"/>
      </svg>
    </div>

    <div class="watercolor-wash" role="img" aria-label="Turquoise watercolour brush strokes"></div>

    <h1 class="kit-title">THE ECLAIR KIT BY</h1>

    <div class="dotted-band" role="img" aria-label="Coral ribbon with white polka dots"></div>

    <div class="brand-label">
      <span class="brand-dot"></span>
      <span class="brand-name">Maison Belle<br>Bakery</span>
    </div>

    <div class="eclair-art left" role="img" aria-label="Illustration of a cream-filled eclair"></div>
    <div class="eclair-art right" role="img" aria-label="Illustration of a cream-filled eclair, cut open"></div>

    <div class="steps-banner">
      <svg width="340" height="80" viewBox="0 0 340 80" aria-hidden="true">
        <polygon points="0,10 340,10 320,40 340,70 0,70 20,40" fill="var(--ribbon)" stroke="var(--ribbon-edge)" stroke-width="2"/>
      </svg>
      <div class="steps-text">3 Simple Steps</div>
    </div>
  </main>
</body>
</html>
```